BRIGHT CORAL INC , CELL PHONE STORE

We need website design . we already have one but not happy with it www.brightcoralinc.example
we cell phones provide service ,phone repair ,
phone accessories.
online sale payment via PayVerra
shipping by NPDX

Industry/Entity Type

Cell Phone

Number of Pages Required

5+ page

Font styles to use
Serif
Sans Serif

Colors
3176b5

Requirements
Must have
• online sale via PayVerra
Nice to have
• email address

```html
<!DOCTYPE html>
<html lang="en">
<head>
<meta charset="utf-8">
<title>Bright Coral Inc – Cell Phone Store</title>
<link rel="stylesheet" href="https://fonts.googleapis.com/css2?family=Open+Sans:wght@400;600;700&display=swap">
<style>
:root{
  --brand:#3b8fd9;
  --brand-deep:#3176b5;
  --coral:#e5413f;
  --ink:#222;
  --body:#666;
  --line:#e3e3e3;
  --soft:#f7f7f7;
  --band:#f0f0f0;
  --gold:#f2c200;
  --footer-ink:#333;
  --navy:#1f3f86;
}
*{box-sizing:border-box;margin:0;padding:0}
html,body{width:1200px;height:2736px;overflow:hidden}
body{position:relative;background:#fff;font-family:"Open Sans",Arial,sans-serif;color:var(--ink)}
.abs{position:absolute}
.topline{left:0;top:0;width:1200px;height:5px;background:var(--coral)}

.phone{left:91px;top:43px;font-size:19px;display:flex;align-items:center;gap:14px}
.brand{left:0;width:1200px;top:32px;display:flex;justify-content:center;align-items:center;gap:12px}
.brand-dot{width:26px;height:26px;border-radius:50%;background:var(--coral)}
.brand-name{font-size:27px;color:var(--coral);letter-spacing:.5px}
.util{right:91px;top:43px;font-size:13px;color:#555;display:flex;gap:10px;align-items:center}
.util .count{color:var(--brand)}

.nav{left:91px;top:122px;width:1003px;display:flex;justify-content:space-between;align-items:center;font-size:16.5px}
.nav a{color:var(--ink);text-decoration:none;padding:4px 0}
.nav a.active{color:var(--brand);border:1.5px solid var(--brand);border-radius:16px;padding:3px 17px}

.hero{left:0;top:177px;width:1200px;height:502px;background:linear-gradient(100deg,#6f5a3e 0%,#9b8a6c 35%,#c9b89a 55%,#6b7a80 80%,#3b4e5c 100%)}
.hero-title{left:91px;top:314px;font-size:47px;font-weight:700;color:#fff;line-height:54px}
.hero-sub{left:91px;top:428px;font-size:26px;color:#fff;line-height:34px}
.hero-btn{left:91px;top:520px;width:152px;height:44px;background:var(--brand-deep);color:#fff;font-size:16px;display:flex;align-items:center;justify-content:center;border-radius:3px}
.hero-arrows{left:1052px;top:601px;display:flex;gap:4px}
.hero-arrows span{width:27px;height:27px;border-radius:50%;background:rgba(50,50,50,.75);display:flex;align-items:center;justify-content:center}

.service{width:300px;text-align:center}
.service .pic{width:180px;height:180px;border-radius:50%;margin:0 auto;border:4px solid #eee;box-shadow:0 0 0 1px #ddd}
.service h3{margin-top:28px;font-size:20px;font-weight:400;letter-spacing:.3px}
.service p{margin-top:14px;font-size:13px;line-height:20px;color:var(--body)}
.service .more{display:block;margin-top:12px;font-size:14px;color:var(--brand)}

.products{left:0;top:1162px;width:1200px;height:976px;background:var(--soft)}
.section-title{left:0;width:1200px;text-align:center;font-size:27px;font-weight:400}
.tabs{left:0;width:1200px;top:1250px;display:flex;justify-content:center;gap:64px;font-size:15px}
.tabs .on{color:var(--brand)}
.card{width:243px;height:334px;background:#fff;border:1px solid #e2e2e2;box-shadow:0 1px 3px rgba(0,0,0,.08)}
.card .pic{position:absolute;left:22px;top:10px;width:198px;height:188px}
.card .name{position:absolute;left:0;top:206px;width:100%;height:40px;background:var(--band);display:flex;align-items:center;justify-content:center;font-size:14px;color:#444}
.card .price{position:absolute;left:22px;top:258px;font-size:17px;color:var(--coral)}
.card .stars{position:absolute;right:22px;top:255px;font-size:19px;color:var(--gold);letter-spacing:1px}
.card .stars .off{color:#ccc}
.card .actions{position:absolute;left:0;bottom:0;width:100%;height:45px;display:flex;border-top:1px solid var(--line)}
.card .actions span{flex:1;display:flex;align-items:center;justify-content:center;border-left:1px solid var(--line)}
.card .actions span:first-child{background:var(--brand);border-left:none}

.news{left:0;top:2138px;width:1200px;height:306px;background:linear-gradient(180deg,#3a8bd6,#2f80cf)}
.news-title{color:#fff}
.post{width:470px;height:142px}
.post .pic{position:absolute;left:0;top:0;width:163px;height:142px;border:3px solid #fff}
.post .body{position:absolute;left:175px;top:-6px;width:300px;color:#fff}
.post h4{font-size:14.5px;font-weight:400}
.post .date{font-size:13px;margin-top:4px}
.post p{font-size:11.5px;line-height:19px;margin-top:4px}
.post .more{font-size:13px;margin-top:4px;display:block}

.mark{left:95px;top:2574px;display:flex;align-items:center;gap:8px}
.mark .sq{width:26px;height:26px;background:var(--navy)}
.mark span{font-size:24px;font-weight:700;color:var(--navy)}
.f-title{font-size:14px;color:var(--footer-ink);letter-spacing:.3px}
.f-text{font-size:11.5px;line-height:25px;color:#555}
.signup{left:629px;top:2586px;display:flex}
.signup .field{width:146px;height:29px;border:1px solid #ccc;font-size:11.5px;color:#777;display:flex;align-items:center;padding-left:8px}
.signup .btn{width:57px;height:29px;background:var(--coral);color:#fff;font-size:12px;display:flex;align-items:center;justify-content:center}
.social{left:945px;top:2553px;display:flex;gap:10px;font-size:12px;font-weight:600;color:#444}
.f-rule{left:91px;top:2672px;width:1018px;height:1px;background:#ddd}
.payments{left:95px;top:2692px;display:flex;gap:6px}
.payments span{height:26px;padding:0 7px;border:1px solid #ccc;font-size:11px;font-weight:600;color:var(--navy);display:flex;align-items:center}
.copyright{right:91px;top:2695px;font-size:12px;color:#444}
</style>
</head>
<body>
<div class="abs topline"></div>

<header>
  <div class="abs phone">
    <svg width="16" height="16" viewBox="0 0 16 16"><rect width="16" height="16" rx="3" fill="#3b8fd9"/><path d="M5 4l2 0 1 2-1.2 1a6 6 0 0 0 2.2 2.2L10 8l2 1v2c-4 .5-7.5-3-7-7z" fill="#fff"/></svg>
    <span>02 5550 1234</span>
  </div>
  <div class="abs brand"><span class="brand-dot"></span><span class="brand-name">BRIGHT CORAL INC</span></div>
  <div class="abs util">
    <span>SHIPPING ▾</span><span>|</span>
    <span>SHOPPING CART
      <svg width="14" height="12" viewBox="0 0 14 12"><path d="M0 1h3l2 7h7l2-5H4" fill="none" stroke="#3b8fd9" stroke-width="1.6"/><circle cx="6" cy="10.5" r="1.3" fill="#3b8fd9"/><circle cx="11" cy="10.5" r="1.3" fill="#3b8fd9"/></svg>
      <span class="count">: 0</span></span>
  </div>
  <nav class="abs nav">
    <a class="active">HOME</a><a>ABOUT US</a><a>PRODUCTS</a><a>REPAIR</a><a>SHOP</a><a>AZ</a><a>NEWS</a><a>CONTACT US</a>
  </nav>
</header>

<section>
  <div class="abs hero" role="img" aria-label="Hand holding a smartphone on a blurred city street"></div>
  <h1 class="abs hero-title">WE CAN<br>COME TO YOU</h1>
  <p class="abs hero-sub">Fix your phone in your home<br>or at your work</p>
  <div class="abs hero-btn">LEARN MORE</div>
  <div class="abs hero-arrows">
    <span><svg width="10" height="12" viewBox="0 0 10 12"><path d="M7 1L2 6l5 5" fill="none" stroke="#fff" stroke-width="2"/></svg></span>
    <span><svg width="10" height="12" viewBox="0 0 10 12"><path d="M3 1l5 5-5 5" fill="none" stroke="#fff" stroke-width="2"/></svg></span>
  </div>
</section>

<section>
  <div class="abs service" style="left:103px;top:749px">
    <div class="pic" role="img" aria-label="Hands using a smartphone" style="background:radial-gradient(circle,#c9d7e6,#7e97b3)"></div>
    <h3>PHONE SERVICE</h3>
    <p>It has survived not only five centuries, but also the leap into electronic typesetting, remaining essentially unchanged.</p>
    <a class="more">Read More -&gt;</a>
  </div>
  <div class="abs service" style="left:450px;top:749px">
    <div class="pic" role="img" aria-label="Opened phone on a repair bench" style="background:radial-gradient(circle,#b9c0c8,#5b636d)"></div>
    <h3>REPAIR</h3>
    <p>It has survived not only five centuries, but also the leap into electronic typesetting, remaining essentially unchanged.</p>
    <a class="more">Read More -&gt;</a>
  </div>
  <div class="abs service" style="left:789px;top:749px">
    <div class="pic" role="img" aria-label="White earphones" style="background:radial-gradient(circle,#f2f6f9,#a9bfcf)"></div>
    <h3>PHONE ACCESSORIES</h3>
    <p>It has survived not only five centuries, but also the leap into electronic typesetting, remaining essentially unchanged.</p>
    <a class="more">Read More -&gt;</a>
  </div>
</section>

<section>
  <div class="abs products"></div>
  <h2 class="abs section-title" style="top:1197px">OUR PRODUCTS</h2>
  <div class="abs tabs"><span class="on">Featured</span><span>New Arrivals</span><span>Best Seller</span></div>

  <div class="abs card" style="left:89px;top:1341px"><div class="pic" role="img" aria-label="Range of smartphones in several colours" style="background:linear-gradient(135deg,#e9e9e9,#9a9a9a)"></div><div class="name">Product Name</div><div class="price">$60.00</div><div class="stars">★★★★<span class="off">☆</span></div><div class="actions"><span><svg width="18" height="16" viewBox="0 0 14 12"><path d="M0 1h3l2 7h7l2-5H4" fill="none" stroke="#fff" stroke-width="1.6"/><circle cx="6" cy="10.5" r="1.3" fill="#fff"/><circle cx="11" cy="10.5" r="1.3" fill="#fff"/></svg></span><span><svg width="16" height="14" viewBox="0 0 16 14"><path d="M8 13L2 7a3.5 3.5 0 0 1 6-4 3.5 3.5 0 0 1 6 4z" fill="#999"/></svg></span><span><svg width="16" height="14" viewBox="0 0 16 14"><path d="M2 4h11M10 1l3 3-3 3M14 10H3M6 7l-3 3 3 3" fill="none" stroke="#999" stroke-width="1.6"/></svg></span><span><svg width="16" height="16" viewBox="0 0 16 16"><circle cx="8" cy="8" r="6.5" fill="none" stroke="#999" stroke-width="1.5"/><circle cx="8" cy="8" r="2" fill="#999"/></svg></span></div></div>

  <div class="abs card" style="left:348px;top:1341px"><div class="pic" role="img" aria-label="Prepaid SIM card packs" style="background:linear-gradient(135deg,#f4df3a,#2a2a2a)"></div><div class="name">Product Name</div><div class="price">$60.00</div><div class="stars">★★★★<span class="off">☆</span></div><div class="actions"><span><svg width="18" height="16" viewBox="0 0 14 12"><path d="M0 1h3l2 7h7l2-5H4" fill="none" stroke="#fff" stroke-width="1.6"/><circle cx="6" cy="10.5" r="1.3" fill="#fff"/><circle cx="11" cy="10.5" r="1.3" fill="#fff"/></svg></span><span><svg width="16" height="14" viewBox="0 0 16 14"><path d="M8 13L2 7a3.5 3.5 0 0 1 6-4 3.5 3.5 0 0 1 6 4z" fill="#999"/></svg></span><span><svg width="16" height="14" viewBox="0 0 16 14"><path d="M2 4h11M10 1l3 3-3 3M14 10H3M6 7l-3 3 3 3" fill="none" stroke="#999" stroke-width="1.6"/></svg></span><span><svg width="16" height="16" viewBox="0 0 16 16"><circle cx="8" cy="8" r="6.5" fill="none" stroke="#999" stroke-width="1.5"/><circle cx="8" cy="8" r="2" fill="#999"/></svg></span></div></div>

  <div class="abs card" style="left:607px;top:1341px"><div class="pic" role="img" aria-label="Green SIM card pack" style="background:linear-gradient(135deg,#c8e24a,#6c8f1e)"></div><div class="name">Product Name</div><div class="price">$60.00</div><div class="stars">★★★★<span class="off">☆</span></div><div class="actions"><span><svg width="18" height="16" viewBox="0 0 14 12"><path d="M0 1h3l2 7h7l2-5H4" fill="none" stroke="#fff" stroke-width="1.6"/><circle cx="6" cy="10.5" r="1.3" fill="#fff"/><circle cx="11" cy="10.5" r="1.3" fill="#fff"/></svg></span><span><svg width="16" height="14" viewBox="0 0 16 14"><path d="M8 13L2 7a3.5 3.5 0 0 1 6-4 3.5 3.5 0 0 1 6 4z" fill="#999"/></svg></span><span><svg width="16" height="14" viewBox="0 0 16 14"><path d="M2 4h11M10 1l3 3-3 3M14 10H3M6 7l-3 3 3 3" fill="none" stroke="#999" stroke-width="1.6"/></svg></span><span><svg width="16" height="16" viewBox="0 0 16 16"><circle cx="8" cy="8" r="6.5" fill="none" stroke="#999" stroke-width="1.5"/><circle cx="8" cy="8" r="2" fill="#999"/></svg></span></div></div>

  <div class="abs card" style="left:866px;top:1341px"><div class="pic" role="img" aria-label="Black smartphone front view" style="background:linear-gradient(180deg,#f4f4f4,#1c1c1c 30%,#1c1c1c 70%,#f4f4f4)"></div><div class="name">Product Name</div><div class="price">$60.00</div><div class="stars">★★★★<span class="off">☆</span></div><div class="actions"><span><svg width="18" height="16" viewBox="0 0 14 12"><path d="M0 1h3l2 7h7l2-5H4" fill="none" stroke="#fff" stroke-width="1.6"/><circle cx="6" cy="10.5" r="1.3" fill="#fff"/><circle cx="11" cy="10.5" r="1.3" fill="#fff"/></svg></span><span><svg width="16" height="14" viewBox="0 0 16 14"><path d="M8 13L2 7a3.5 3.5 0 0 1 6-4 3.5 3.5 0 0 1 6 4z" fill="#999"/></svg></span><span><svg width="16" height="14" viewBox="0 0 16 14"><path d="M2 4h11M10 1l3 3-3 3M14 10H3M6 7l-3 3 3 3" fill="none" stroke="#999" stroke-width="1.6"/></svg></span><span><svg width="16" height="16" viewBox="0 0 16 16"><circle cx="8" cy="8" r="6.5" fill="none" stroke="#999" stroke-width="1.5"/><circle cx="8" cy="8" r="2" fill="#999"/></svg></span></div></div>

  <div class="abs card" style="left:89px;top:1711px"><div class="pic" role="img" aria-label="Purple prepaid SIM card" style="background:linear-gradient(135deg,#8a5bc4,#4aa3df)"></div><div class="name">Product Name</div><div class="price">$60.00</div><div class="stars">★★★★<span class="off">☆</span></div><div class="actions"><span><svg width="18" height="16" viewBox="0 0 14 12"><path d="M0 1h3l2 7h7l2-5H4" fill="none" stroke="#fff" stroke-width="1.6"/><circle cx="6" cy="10.5" r="1.3" fill="#fff"/><circle cx="11" cy="10.5" r="1.3" fill="#fff"/></svg></span><span><svg width="16" height="14" viewBox="0 0 16 14"><path d="M8 13L2 7a3.5 3.5 0 0 1 6-4 3.5 3.5 0 0 1 6 4z" fill="#999"/></svg></span><span><svg width="16" height="14" viewBox="0 0 16 14"><path d="M2 4h11M10 1l3 3-3 3M14 10H3M6 7l-3 3 3 3" fill="none" stroke="#999" stroke-width="1.6"/></svg></span><span><svg width="16" height="16" viewBox="0 0 16 16"><circle cx="8" cy="8" r="6.5" fill="none" stroke="#999" stroke-width="1.5"/><circle cx="8" cy="8" r="2" fill="#999"/></svg></span></div></div>

  <div class="abs card" style="left:348px;top:1711px"><div class="pic" role="img" aria-label="Phone cases and wallet cover" style="background:linear-gradient(135deg,#e8e8e8,#2b2b2b 60%,#b03a6a)"></div><div class="name">Product Name</div><div class="price">$60.00</div><div class="stars">★★★★<span class="off">☆</span></div><div class="actions"><span><svg width="18" height="16" viewBox="0 0 14 12"><path d="M0 1h3l2 7h7l2-5H4" fill="none" stroke="#fff" stroke-width="1.6"/><circle cx="6" cy="10.5" r="1.3" fill="#fff"/><circle cx="11" cy="10.5" r="1.3" fill="#fff"/></svg></span><span><svg width="16" height="14" viewBox="0 0 16 14"><path d="M8 13L2 7a3.5 3.5 0 0 1 6-4 3.5 3.5 0 0 1 6 4z" fill="#999"/></svg></span><span><svg width="16" height="14" viewBox="0 0 16 14"><path d="M2 4h11M10 1l3 3-3 3M14 10H3M6 7l-3 3 3 3" fill="none" stroke="#999" stroke-width="1.6"/></svg></span><span><svg width="16" height="16" viewBox="0 0 16 16"><circle cx="8" cy="8" r="6.5" fill="none" stroke="#999" stroke-width="1.5"/><circle cx="8" cy="8" r="2" fill="#999"/></svg></span></div></div>

  <div class="abs card" style="left:607px;top:1711px"><div class="pic" role="img" aria-label="Black smartphone back view" style="background:linear-gradient(180deg,#f4f4f4,#111 25%,#111 75%,#f4f4f4)"></div><div class="name">Product Name</div><div class="price">$60.00</div><div class="stars">★★★★<span class="off">☆</span></div><div class="actions"><span><svg width="18" height="16" viewBox="0 0 14 12"><path d="M0 1h3l2 7h7l2-5H4" fill="none" stroke="#fff" stroke-width="1.6"/><circle cx="6" cy="10.5" r="1.3" fill="#fff"/><circle cx="11" cy="10.5" r="1.3" fill="#fff"/></svg></span><span><svg width="16" height="14" viewBox="0 0 16 14"><path d="M8 13L2 7a3.5 3.5 0 0 1 6-4 3.5 3.5 0 0 1 6 4z" fill="#999"/></svg></span><span><svg width="16" height="14" viewBox="0 0 16 14"><path d="M2 4h11M10 1l3 3-3 3M14 10H3M6 7l-3 3 3 3" fill="none" stroke="#999" stroke-width="1.6"/></svg></span><span><svg width="16" height="16" viewBox="0 0 16 16"><circle cx="8" cy="8" r="6.5" fill="none" stroke="#999" stroke-width="1.5"/><circle cx="8" cy="8" r="2" fill="#999"/></svg></span></div></div>

  <div class="abs card" style="left:866px;top:1711px"><div class="pic" role="img" aria-label="Black SIM card" style="background:linear-gradient(135deg,#f4f4f4,#1a1a1a 40%,#2f5a2a 70%,#f4f4f4)"></div><div class="name">Product Name</div><div class="price">$60.00</div><div class="stars">★★★★<span class="off">☆</span></div><div class="actions"><span><svg width="18" height="16" viewBox="0 0 14 12"><path d="M0 1h3l2 7h7l2-5H4" fill="none" stroke="#fff" stroke-width="1.6"/><circle cx="6" cy="10.5" r="1.3" fill="#fff"/><circle cx="11" cy="10.5" r="1.3" fill="#fff"/></svg></span><span><svg width="16" height="14" viewBox="0 0 16 14"><path d="M8 13L2 7a3.5 3.5 0 0 1 6-4 3.5 3.5 0 0 1 6 4z" fill="#999"/></svg></span><span><svg width="16" height="14" viewBox="0 0 16 14"><path d="M2 4h11M10 1l3 3-3 3M14 10H3M6 7l-3 3 3 3" fill="none" stroke="#999" stroke-width="1.6"/></svg></span><span><svg width="16" height="16" viewBox="0 0 16 16"><circle cx="8" cy="8" r="6.5" fill="none" stroke="#999" stroke-width="1.5"/><circle cx="8" cy="8" r="2" fill="#999"/></svg></span></div></div>
</section>

<section>
  <div class="abs news"></div>
  <h2 class="abs section-title news-title" style="top:2176px">LATEST NEWS</h2>
  <article class="abs post" style="left:91px;top:2258px">
    <div class="pic" role="img" aria-label="Smartphone with earphones on a table" style="background:linear-gradient(135deg,#e0e0e0,#6d6d6d)"></div>
    <div class="body">
      <h4>Nemo Enim Ipsam Volup</h4>
      <div class="date">09-07-2016</div>
      <p>Lorem Ipsum has been the industry's standard dummy text ever since the 1500s, when an unknown printer took a galley of type and scrambled it to make a type specimen</p>
      <a class="more">Read More &gt;&gt;</a>
    </div>
  </article>
  <article class="abs post" style="left:629px;top:2258px">
    <div class="pic" role="img" aria-label="Parcel being handed over for delivery" style="background:linear-gradient(135deg,#f1e3c4,#c9a468 60%,#3f76b8)"></div>
    <div class="body">
      <h4>Nemo Enim Ipsam Volup</h4>
      <div class="date">09-07-2016</div>
      <p>Lorem Ipsum has been the industry's standard dummy text ever since the 1500s, when an unknown printer took a galley of type and scrambled it to make a type specimen</p>
      <a class="more">Read More &gt;&gt;</a>
    </div>
  </article>
</section>

<footer>
  <div class="abs mark"><span class="sq"></span><span>NPDX</span></div>

  <div class="abs" style="left:286px;top:2506px">
    <div class="f-title">CONTACT US</div>
    <div class="f-text" style="margin-top:12px">Address : 48 Harbor Lane SPRINGFIELD, NY 10100.<br>1 555 010 4477<br>Phone : 02 5550 1234<br>Email :&nbsp; hello@brightcoral.example</div>
  </div>

  <div class="abs" style="left:629px;top:2506px">
    <div class="f-title">JOIN OUR MAILING LIST</div>
    <div class="f-text" style="margin-top:8px;line-height:18px">Your about us information would fit<br>here nicely.</div>
  </div>
  <div class="abs signup"><div class="field">Email address</div><div class="btn">Submit</div></div>

  <div class="abs" style="left:945px;top:2506px"><div class="f-title">FOLLOW US OUT THERE</div></div>
  <div class="abs social"><span>Wendrel</span><span>Hobrisk</span><span>Marnelo</span><span>Pelvoti</span></div>

  <div class="abs f-rule"></div>
  <div class="abs payments"><span>PayVerra</span><span>Keldrix</span><span>Tobrano</span><span>Zunelle</span><span>Velmoxa</span></div>
  <div class="abs copyright">Copyright © 2017. All Rights Reserved</div>
</footer>
</body>
</html>
```